Photo Storage Service - Web Application

This is web design for a simple photo storage service.
There is a web page and on the left side is a list of folders and on the right side there are photo thumbnails. By pressing a photo thumbnail, they will see the full size (it's just a link to a different page).
This project is limited only to ONE page, which is the page with the folders list and the thumbnails. However it contains some features that I will try to list here:
- Name of the service: Tavo Vault
- Location of account: http://username.tavo.example
- Folder list: Show all folders belonging to the user. Because you have to be able to drag photos to a folder, they have to be visible and cannot be hidden behind a menu item etc.
- Thumbnails with photos (in the future also videos)
- Adjusted view with smaller thumbnails and less space for folder list (so it is possible to view a larger quantity of thumbnails)- Select multiple thumbnails with rectangle- Show that a thumbnail is selected (maybe bold border?)
- Simple mobile view, but no emphasis on the mobile view in this design project.
- Drag one or more selected photos to a folder
- Delete one or more selected photos
- Drag a folder to another folder
- Rename folder
- Delete folder
- Create folder
- Show progress when deleting/moving (because it calls for every photo, so if there are 100 photos, it will delete 1 by 1 and it will take about 10 seconds - you could show progress bar or equivalent)
Background information: This is for a photo storage service NOT intended for sharing photos, but intended to indefinitely store photos and for yourself to browse your own photos.
It is a design requirement that it loads extremely fast. So we need to limit as much as possible extra graphics that cannot be done by CSS and other external libraries.
(I know this is ONLY design and nothing to do with CSS or libraries, but I can assess from the design if it might be heavy to load when implemented)
I have attached a crude screenshot of the current design, just for your understanding. It should not match this design and you are not in any way supposed to FIT your design into this same style or structure.
Target Market(s)
Consumers
Number of Pages Required
1 page
Font styles to use
Look and feel
Each slider illustrates characteristics of the customer's brand and the style your logo design should communicate.

```html
<!DOCTYPE html>
<html lang="en">
<head>
<meta charset="utf-8">
<title>Tavo Vault</title>
<link rel="stylesheet" href="https://fonts.googleapis.com/css2?family=Raleway:wght@500;600;700&family=Open+Sans:wght@400;700&display=swap">
<style>
  :root {
    --navy: #1f2f6b;
    --page: #e8ebf2;
    --white: #ffffff;
    --orange: #f05a1c;
    --text: #2a2f45;
    --footer: #161616;
  }
  * { box-sizing: border-box; margin: 0; padding: 0; }
  html, body { width: 854px; height: 1200px; overflow: hidden; }
  body { background: var(--page); font-family: "Raleway", sans-serif; position: relative; }

  .topbar { position: absolute; left: 0; top: 0; width: 854px; height: 66px; background: var(--navy); }
  .brand { position: absolute; left: 70px; top: 17px; display: flex; align-items: center; gap: 9px; color: var(--white); font-weight: 700; font-size: 15px; letter-spacing: 0.2px; text-transform: uppercase; }
  .brand-dot { width: 30px; height: 30px; border-radius: 50%; background: var(--white); }
  .btn-outline { position: absolute; top: 14px; height: 37px; border: 1.5px solid var(--white); border-radius: 19px; color: var(--white); font-family: "Open Sans", sans-serif; font-weight: 700; font-size: 12px; display: flex; align-items: center; justify-content: center; gap: 6px; letter-spacing: 0.2px; }
  .btn-upload { left: 465px; width: 135px; }
  .btn-delete { left: 612px; width: 172px; }

  .folders { position: absolute; left: 70px; top: 130px; width: 189px; height: 943px; background: var(--white); box-shadow: 0 1px 3px rgba(0,0,0,0.06); padding: 147px 0 0; padding-top: 17px; list-style: none; }
  .folder { display: flex; align-items: flex-start; gap: 6px; padding-left: 15px; font-size: 12.4px; font-weight: 500; line-height: 17.6px; color: var(--text); margin-bottom: 17.8px; white-space: nowrap; font-variant-numeric: oldstyle-nums; }
  .folder svg { flex: none; margin-top: 3px; }
  .folder.active { color: var(--orange); }

  .thumb { position: absolute; width: 151px; height: 127px; border: 2px solid var(--white); box-shadow: 0 1px 3px rgba(0,0,0,0.15); }

  .view-more { position: absolute; left: 475px; top: 1023px; width: 129px; height: 46px; border-radius: 23px; background: var(--orange); color: var(--white); font-family: "Open Sans", sans-serif; font-weight: 700; font-size: 13.5px; display: flex; align-items: center; justify-content: center; letter-spacing: 0.3px; }

  .footer { position: absolute; left: 0; top: 1142px; width: 854px; height: 58px; background: var(--footer); color: var(--white); font-family: "Open Sans", sans-serif; font-size: 10px; display: flex; align-items: center; justify-content: center; }
</style>
</head>
<body>
  <header class="topbar">
    <div class="brand"><span class="brand-dot"></span>Tavo Vault</div>
    <div class="btn-outline btn-upload">
      <svg width="11" height="11" viewBox="0 0 12 12"><path d="M6 1 L10 5 H7.5 V8.5 H4.5 V5 H2 Z" fill="#fff"/><rect x="1" y="9.5" width="10" height="1.6" fill="#fff"/></svg>
      UPLOAD FILES
    </div>
    <div class="btn-outline btn-delete">
      <svg width="9" height="11" viewBox="0 0 10 12"><rect x="0.5" y="1.5" width="9" height="1.4" fill="#fff"/><rect x="3.5" y="0" width="3" height="1.6" fill="#fff"/><path d="M1.5 3.5 H8.5 L8 11.5 H2 Z" fill="none" stroke="#fff" stroke-width="1.2"/></svg>
      DELETE SELECTED FILES
    </div>
  </header>

  <ul class="folders">
    <li class="folder active"><svg width="11" height="11" viewBox="0 0 12 12"><circle cx="6" cy="6" r="6" fill="#f05a1c"/><path d="M3.2 6.2 L5.2 8 L8.8 4.2" stroke="#fff" stroke-width="1.6" fill="none"/></svg><span>Inbox</span></li>
    <li class="folder"><svg width="11" height="11" viewBox="0 0 12 12"><circle cx="6" cy="6" r="6" fill="#1f2f6b"/><path d="M3.2 6.2 L5.2 8 L8.8 4.2" stroke="#fff" stroke-width="1.6" fill="none"/></svg><span>80s party</span></li>
    <li class="folder"><svg width="11" height="11" viewBox="0 0 12 12"><circle cx="6" cy="6" r="6" fill="#1f2f6b"/><path d="M3.2 6.2 L5.2 8 L8.8 4.2" stroke="#fff" stroke-width="1.6" fill="none"/></svg><span>A day in Oslo</span></li>
    <li class="folder"><svg width="11" height="11" viewBox="0 0 12 12"><circle cx="6" cy="6" r="6" fill="#1f2f6b"/><path d="M3.2 6.2 L5.2 8 L8.8 4.2" stroke="#fff" stroke-width="1.6" fill="none"/></svg><span>A tour of Svendborg<br>Alicante 2017</span></li>
    <li class="folder"><svg width="11" height="11" viewBox="0 0 12 12"><circle cx="6" cy="6" r="6" fill="#1f2f6b"/><path d="M3.2 6.2 L5.2 8 L8.8 4.2" stroke="#fff" stroke-width="1.6" fill="none"/></svg><span>Alicante after Christmas</span></li>
    <li class="folder"><svg width="11" height="11" viewBox="0 0 12 12"><circle cx="6" cy="6" r="6" fill="#1f2f6b"/><path d="M3.2 6.2 L5.2 8 L8.8 4.2" stroke="#fff" stroke-width="1.6" fill="none"/></svg><span>Bandarban</span></li>
    <li class="folder"><svg width="11" height="11" viewBox="0 0 12 12"><circle cx="6" cy="6" r="6" fill="#1f2f6b"/><path d="M3.2 6.2 L5.2 8 L8.8 4.2" stroke="#fff" stroke-width="1.6" fill="none"/></svg><span>Birds lightly garnished with<br>monkeys and waterfalls</span></li>
    <li class="folder"><svg width="11" height="11" viewBox="0 0 12 12"><circle cx="6" cy="6" r="6" fill="#1f2f6b"/><path d="M3.2 6.2 L5.2 8 L8.8 4.2" stroke="#fff" stroke-width="1.6" fill="none"/></svg><span>Brazil</span></li>
    <li class="folder"><svg width="11" height="11" viewBox="0 0 12 12"><circle cx="6" cy="6" r="6" fill="#1f2f6b"/><path d="M3.2 6.2 L5.2 8 L8.8 4.2" stroke="#fff" stroke-width="1.6" fill="none"/></svg><span>Days in Denmark -<br>Christmas and new years</span></li>
    <li class="folder"><svg width="11" height="11" viewBox="0 0 12 12"><circle cx="6" cy="6" r="6" fill="#1f2f6b"/><path d="M3.2 6.2 L5.2 8 L8.8 4.2" stroke="#fff" stroke-width="1.6" fill="none"/></svg><span>Mobile Uploads</span></li>
    <li class="folder"><svg width="11" height="11" viewBox="0 0 12 12"><circle cx="6" cy="6" r="6" fill="#1f2f6b"/><path d="M3.2 6.2 L5.2 8 L8.8 4.2" stroke="#fff" stroke-width="1.6" fill="none"/></svg><span>Random</span></li>
    <li class="folder"><svg width="11" height="11" viewBox="0 0 12 12"><circle cx="6" cy="6" r="6" fill="#1f2f6b"/><path d="M3.2 6.2 L5.2 8 L8.8 4.2" stroke="#fff" stroke-width="1.6" fill="none"/></svg><span>Recently uploaded<br>from phone</span></li>
    <li class="folder"><svg width="11" height="11" viewBox="0 0 12 12"><circle cx="6" cy="6" r="6" fill="#1f2f6b"/><path d="M3.2 6.2 L5.2 8 L8.8 4.2" stroke="#fff" stroke-width="1.6" fill="none"/></svg><span>Sundarban</span></li>
    <li class="folder"><svg width="11" height="11" viewBox="0 0 12 12"><circle cx="6" cy="6" r="6" fill="#1f2f6b"/><path d="M3.2 6.2 L5.2 8 L8.8 4.2" stroke="#fff" stroke-width="1.6" fill="none"/></svg><span>Sylhet ll</span></li>
    <li class="folder"><svg width="11" height="11" viewBox="0 0 12 12"><circle cx="6" cy="6" r="6" fill="#1f2f6b"/><path d="M3.2 6.2 L5.2 8 L8.8 4.2" stroke="#fff" stroke-width="1.6" fill="none"/></svg><span>Tea Garden</span></li>
    <li class="folder"><svg width="11" height="11" viewBox="0 0 12 12"><circle cx="6" cy="6" r="6" fill="#1f2f6b"/><path d="M3.2 6.2 L5.2 8 L8.8 4.2" stroke="#fff" stroke-width="1.6" fill="none"/></svg><span>Thailand 1</span></li>
    <li class="folder"><svg width="11" height="11" viewBox="0 0 12 12"><circle cx="6" cy="6" r="6" fill="#1f2f6b"/><path d="M3.2 6.2 L5.2 8 L8.8 4.2" stroke="#fff" stroke-width="1.6" fill="none"/></svg><span>Thailand 2</span></li>
    <li class="folder"><svg width="11" height="11" viewBox="0 0 12 12"><circle cx="6" cy="6" r="6" fill="#1f2f6b"/><path d="M3.2 6.2 L5.2 8 L8.8 4.2" stroke="#fff" stroke-width="1.6" fill="none"/></svg><span>Thailand 2018</span></li>
    <li class="folder"><svg width="11" height="11" viewBox="0 0 12 12"><circle cx="6" cy="6" r="6" fill="#1f2f6b"/><path d="M3.2 6.2 L5.2 8 L8.8 4.2" stroke="#fff" stroke-width="1.6" fill="none"/></svg><span>Timeline Photos</span></li>
    <li class="folder"><svg width="11" height="11" viewBox="0 0 12 12"><circle cx="6" cy="6" r="6" fill="#1f2f6b"/><path d="M3.2 6.2 L5.2 8 L8.8 4.2" stroke="#fff" stroke-width="1.6" fill="none"/></svg><span>USA</span></li>
    <li class="folder"><svg width="11" height="11" viewBox="0 0 12 12"><circle cx="6" cy="6" r="6" fill="#1f2f6b"/><path d="M3.2 6.2 L5.2 8 L8.8 4.2" stroke="#fff" stroke-width="1.6" fill="none"/></svg><span>UploadBag</span></li>
    <li class="folder"><svg width="11" height="11" viewBox="0 0 12 12"><circle cx="6" cy="6" r="6" fill="#1f2f6b"/><path d="M3.2 6.2 L5.2 8 L8.8 4.2" stroke="#fff" stroke-width="1.6" fill="none"/></svg><span>Vancouver</span></li>
    <li class="folder"><svg width="11" height="11" viewBox="0 0 12 12"><circle cx="6" cy="6" r="6" fill="#1f2f6b"/><path d="M3.2 6.2 L5.2 8 L8.8 4.2" stroke="#fff" stroke-width="1.6" fill="none"/></svg><span>Thumbnails</span></li>
    <li class="folder"><svg width="11" height="11" viewBox="0 0 12 12"><circle cx="6" cy="6" r="6" fill="#1f2f6b"/><path d="M3.2 6.2 L5.2 8 L8.8 4.2" stroke="#fff" stroke-width="1.6" fill="none"/></svg><span>Videos/Thumbnails</span></li>
  </ul>

  <main class="gallery">
    <div class="thumb" role="img" aria-label="Clock tower on a harbour pier at sunset" style="left:295px;top:130px;background:linear-gradient(180deg,#c9a27a,#e3a05a 55%,#6a5646)"></div>
    <div class="thumb" role="img" aria-label="City square with trees and a bus under blue sky" style="left:463px;top:130px;background:linear-gradient(180deg,#3f72c9,#6e8e4a 55%,#4a4640)"></div>
    <div class="thumb" role="img" aria-label="Lighthouse on a rocky coast with sun" style="left:631px;top:130px;background:linear-gradient(160deg,#a8c4de,#e8d08a 45%,#4e5a3a)"></div>

    <div class="thumb" role="img" aria-label="Icy harbour with a wooden jetty" style="left:295px;top:275px;background:linear-gradient(180deg,#1e3a8c,#3c5fa8 55%,#5a6a80)"></div>
    <div class="thumb" role="img" aria-label="Tropical beach with palm trees" style="left:463px;top:275px;background:linear-gradient(180deg,#3b8bd0,#2fb5c0 40%,#e8e2d2 65%,#3f7a2a)"></div>
    <div class="thumb" role="img" aria-label="Suspension bridge in a misty forest" style="left:631px;top:275px;background:linear-gradient(180deg,#8a9080,#4c5a3c 60%,#2a2e24)"></div>

    <div class="thumb" role="img" aria-label="Red and white lighthouse in dune grass" style="left:295px;top:420px;background:linear-gradient(180deg,#3d7ed6,#9ec2e6 45%,#9aa048 65%,#6f7a2c)"></div>
    <div class="thumb" role="img" aria-label="Glass office buildings from below" style="left:463px;top:420px;background:linear-gradient(180deg,#6f8fb8,#2e3e5a 55%,#3a4a3a)"></div>
    <div class="thumb" role="img" aria-label="Statue on an island in front of a city skyline" style="left:631px;top:420px;background:linear-gradient(180deg,#3e5c8a,#8aa2c0 60%,#2a3e5a)"></div>

    <div class="thumb" role="img" aria-label="Snowy entrance at dusk" style="left:295px;top:566px;background:linear-gradient(180deg,#7a8090,#2a3250 55%,#1c2030)"></div>
    <div class="thumb" role="img" aria-label="Tunnel with coloured lights" style="left:463px;top:566px;background:linear-gradient(100deg,#5a5650,#7a746a 50%,#3a9a6a 80%,#1f6a4a)"></div>
    <div class="thumb" role="img" aria-label="Dimly lit restaurant interior" style="left:631px;top:566px;background:linear-gradient(180deg,#4a3a2e,#2a2018 60%,#3a2a1e)"></div>

    <div class="thumb" role="img" aria-label="Waterfront square at sunset" style="left:295px;top:711px;background:linear-gradient(180deg,#d8c0b0,#a88e7e 45%,#4a4040)"></div>
    <div class="thumb" role="img" aria-label="Modern building by the water at dusk" style="left:463px;top:711px;background:linear-gradient(180deg,#c8b0a0,#8e8480 45%,#4a4446)"></div>
    <div class="thumb" role="img" aria-label="City hall at night with passing car" style="left:631px;top:711px;background:linear-gradient(180deg,#2a2018,#6a4a24 50%,#1a1a20)"></div>

    <div class="thumb" role="img" aria-label="Harbour with a domed science building" style="left:295px;top:856px;background:linear-gradient(180deg,#1f6ad0,#c8d4e0 45%,#2c5ea0 70%,#6a6050)"></div>
    <div class="thumb" role="img" aria-label="Castle with formal gardens" style="left:463px;top:856px;background:linear-gradient(180deg,#5a9ae0,#8a6a50 40%,#7a9a2a 60%,#4a5a1a)"></div>
    <div class="thumb" role="img" aria-label="Winter street scene in red tones" style="left:631px;top:856px;background:linear-gradient(180deg,#8a9ab8,#a04040 55%,#6a5a60)"></div>
  </main>

  <div class="view-more">VIEW MORE</div>

  <footer class="footer">Copyright © 2018, Tavo Vault . All rights reserved.</footer>
</body>
</html>
```